2nd Generation Blind Manufacturer & Retailer Needs A Stationary Set

We need a stationary set for a family business located the in the Whitsundays (QLD). We retail and manufacture blinds awnings and shutters. Second generation, in operation for over 30 years.

Final draft must include at minimum:

Business Card (2 Sided)
Letterhead
Presentation Folder

Target Market(s)

home owners, landlords, builders, real estate agents, shopping centres

Industry/Entity Type

Textile

Requirements
Must have
• Design needs to work in mono as well as colour print
Nice to have
• Relevant to the textile industry
Should not have
• The inclusion of blinds, awnings or shutters is an automatic no-no

```html
<!DOCTYPE html>
<html lang="en">
<head>
<meta charset="utf-8">
<title>Tindall Blinds – Stationery Set</title>
<link rel="stylesheet" href="https://fonts.googleapis.com/css2?family=Arimo:wght@400;600&family=Open+Sans:wght@400;600&family=Yellowtail&display=swap">
<style>
  :root{
    --canvas:#e3e3e5;
    --paper:#ffffff;
    --slate:#6d6d6f;
    --slate-soft:#7a7a7c;
    --plum:#7b2a7e;
    --ink:#1d1d1d;
    --brand-grey:#6b6b6d;
    --spine:#d9d9db;
  }
  *{margin:0;padding:0;box-sizing:border-box}
  html,body{width:1189px;height:1200px;overflow:hidden;background:var(--canvas)}
  body{position:relative;font-family:"Open Sans",Arial,sans-serif}
  .piece{position:absolute;background:var(--paper);overflow:hidden}

  /* brand block */
  .brand{position:absolute;display:flex;align-items:center;gap:8px}
  .brand-square{width:42px;height:42px;background:var(--brand-grey)}
  .brand-rule{width:1px;align-self:stretch;background:var(--brand-grey)}
  .brand-name{font-family:"Open Sans",Arial,sans-serif;font-weight:600;color:var(--brand-grey);
    text-transform:uppercase;letter-spacing:1.5px;line-height:.95;font-size:22px}
  .brand.light .brand-square,.brand.light .brand-rule{background:#fff}
  .brand.light .brand-name{color:#fff}

  /* letterhead */
  .letterhead{left:72px;top:100px;width:508px;height:657px;font-family:"Arimo",Arial,sans-serif;color:var(--ink)}
  .letterhead .brand{left:40px;top:40px;height:68px}
  .lh-contact{position:absolute;right:40px;top:59px;font-family:"Open Sans",sans-serif;font-size:7.5px;
    color:#777;text-align:right;line-height:9.5px}
  .lh-contact span{display:inline-block;width:7px;height:7px;background:var(--plum);margin-left:5px;vertical-align:-1px}
  .recipient{position:absolute;left:40px;top:186px;font-size:8.6px;line-height:10.5px}
  .recipient strong{display:block;font-size:10px;font-weight:600;margin-bottom:3px}
  .body-copy{position:absolute;left:40px;top:258px;width:432px;font-size:8.7px;line-height:14.9px;color:var(--ink)}
  .body-copy p+p{margin-top:14.9px}
  .signoff{position:absolute;left:40px;top:495px;font-size:9.2px}
  .signature{position:absolute;left:38px;top:508px;font-family:"Yellowtail",cursive;font-size:34px;line-height:40px;color:var(--ink)}
  .signer{position:absolute;left:40px;top:558px;font-size:9.2px;line-height:12px}
  .signer strong{display:block;font-weight:600;font-size:10px}
  .lh-footer{position:absolute;left:0;top:610px;width:100%;height:33px;background:var(--slate);
    color:#eee;font-family:"Open Sans",sans-serif;font-size:8px;text-align:center;line-height:33px}
  .lh-strip{position:absolute;left:0;top:643px;width:100%;height:14px;background:var(--plum)}

  /* folder */
  .folder{left:610px;top:100px;width:506px;height:653px}
  .folder .brand{left:150px;top:96px;height:72px}
  .folder-field{position:absolute;left:0;top:230px;width:100%;height:344px;
    background:radial-gradient(circle at 70% 30%,var(--slate-soft),var(--slate) 70%)}
  .folder-base{position:absolute;left:0;top:574px;width:100%;height:79px;background:var(--plum);
    color:#eee;font-size:8px;text-align:center;padding-top:36px}
  .spine{position:absolute;left:26px;top:0;width:3px;height:100%;background:var(--spine);opacity:.7}

  /* business cards */
  .card-front{left:149px;top:860px;width:353px;height:201px}
  .card-front .brand{left:84px;top:22px;height:66px}
  .card-band{position:absolute;left:0;top:111px;width:100%;height:70px;background:var(--slate);color:#fff}
  .card-person{position:absolute;right:194px;top:20px;text-align:right;line-height:11px}
  .card-person strong{display:block;font-weight:600;font-size:13px;line-height:15px}
  .card-person span{font-size:9.5px}
  .card-divider{position:absolute;left:172px;top:17px;width:1px;height:36px;background:#fff}
  .card-contact{position:absolute;left:186px;top:17px;font-size:9.5px;line-height:12.5px}
  .card-contact i{display:inline-block;width:8px;height:8px;background:var(--plum);margin-right:5px;vertical-align:-1px}
  .card-foot{position:absolute;left:0;top:181px;width:100%;height:20px;background:var(--plum);
    color:#fff;font-size:10px;text-align:center;line-height:20px}

  .card-back{left:687px;top:860px;width:351px;height:200px;background:var(--slate)}
  .card-back .card-field{position:absolute;inset:0 0 21px 0;
    background:radial-gradient(circle at 75% 20%,var(--slate-soft),var(--slate) 70%)}
  .card-back .brand{left:86px;top:67px;height:64px}
  .card-back .card-foot{top:179px;height:21px;line-height:21px;font-weight:600}
</style>
</head>
<body>

<section class="piece letterhead">
  <div class="brand">
    <div class="brand-square"></div><div class="brand-rule"></div>
    <div class="brand-name">Tindall<br>Blinds</div>
  </div>
  <div class="lh-contact">
    123 456 7890<span></span><br>your@yourcompany.com<span></span><br>www.yourcompany.com<span></span>
  </div>
  <div class="recipient"><strong>JOHN SMITH</strong>Street Name,City Name.<br>Zip Coad 0000</div>
  <div class="body-copy">
    <p>Lorem Ipsum is simply dummy text of the printing and typesetting industry. Lorem Ipsum has been the industry's standard dummy text ever since the 1500s, when an unknown printer took a galley of type and scrambled it to make a type specimen book. It has survived not only five centuries, but also the leap into electronic typesetting, remaining essentially unchanged. It was popularised in the 1960s with the release of Letraset sheets containing Lorem Ipsum passages, and more recently with desktop publishing software like Aldus PageMaker including versions of Lorem Ipsum.</p>
    <p>It is a long established fact that a reader will be distracted by the readable content of a page when looking at its layout. The point of using Lorem Ipsum is that it has a more-or-less normal distribution of letters, as opposed to using 'Content here, content here', making it look like readable English. Many desktop publishing packages and web page editors now use Lorem Ipsum as their default model text, and a search for 'lorem ipsum' will uncover many web sites still in their infancy. Various versions have evolved over the years, sometimes by accident, sometimes on purpose (injected humour and the like).</p>
  </div>
  <div class="signoff">Regards,</div>
  <div class="signature">John Doe</div>
  <div class="signer"><strong>John Doe</strong>General Maneger</div>
  <div class="lh-footer">0000 Youe Address,2nd Ste. Larkmoor, Westvale 1234</div>
  <div class="lh-strip"></div>
</section>

<section class="piece folder">
  <div class="brand">
    <div class="brand-square"></div><div class="brand-rule"></div>
    <div class="brand-name" style="font-size:25px">Tindall<br>Blinds</div>
  </div>
  <div class="folder-field" role="img" aria-label="Large faint brand symbol pattern in soft grey"></div>
  <div class="folder-base">www.yourwebsite.com</div>
  <div class="spine"></div>
</section>

<section class="piece card-front">
  <div class="brand">
    <div class="brand-square"></div><div class="brand-rule"></div>
    <div class="brand-name">Tindall<br>Blinds</div>
  </div>
  <div class="card-band">
    <div class="card-person"><strong>Jhone Smith</strong><span>Principal</span></div>
    <div class="card-divider"></div>
    <div class="card-contact">
      <i></i>000 000 0000<br><i></i>yourcompany@gmail.com<br><i></i>www.yourcompany.com
    </div>
  </div>
  <div class="card-foot">0000 Youe Address,2nd Ste. Larkmoor, Westvale 1234</div>
</section>

<section class="piece card-back">
  <div class="card-field" role="img" aria-label="Large faint brand symbol pattern in soft grey"></div>
  <div class="brand light">
    <div class="brand-square"></div><div class="brand-rule"></div>
    <div class="brand-name">Tindall<br>Blinds</div>
  </div>
  <div class="card-foot">www.yourcompany.com</div>
</section>

</body>
</html>
```